Personal Development Brand Needs a Workbook Cover Design

We need a clean and sleek cover design for our A4-Sized workbook called the "12-Week Horizon Logbook"

There's around 90 pages in the workbook, if that matters for the spine.

Necessary Elements on the Front Cover:

- Logo
- Title: Peak Lantern Horizon Logbook
- Subtitle: A Simple Workbook to Track Your Transformation
- Author Name: Dale Wrenfold

Elements on Back Cover:

- The Peak Lantern Creed

```html
<!DOCTYPE html>
<html lang="en">
<head>
<meta charset="utf-8">
<title>Peak Lantern Horizon Logbook – Cover Spread</title>
<link rel="stylesheet" href="https://fonts.googleapis.com/css2?family=Oswald:wght@400;500;600&family=Jost:wght@300;400&family=Noto+Sans:wght@700;800&display=swap">
<style>
  :root {
    --slate-dark: #2b333d;
    --slate-mid: #3a4450;
    --slate-light: #566372;
    --signal-red: #e0382c;
    --signal-red-deep: #c92f25;
    --gold-light: #e2bb90;
    --gold-dark: #b4875c;
    --title-pale: #d3dce3;
    --ink-white: #ffffff;
    --page: #ffffff;
  }
  html, body {
    margin: 0;
    padding: 0;
    width: 877px;
    height: 1200px;
    overflow: hidden;
    background: var(--page);
  }
  .cover-spread {
    position: absolute;
    left: 20px;
    top: 306px;
    width: 1105px;
    height: 775px;
    transform: scale(0.7575);
    transform-origin: top left;
    overflow: hidden;
    background:
      radial-gradient(ellipse 60% 55% at 50% 0%, var(--slate-light) 0%, transparent 70%),
      linear-gradient(180deg, var(--slate-mid) 0%, var(--slate-dark) 100%);
  }
  .cover-art {
    position: absolute;
    inset: 0;
    width: 1105px;
    height: 775px;
  }
  .back-cover {
    position: absolute;
    left: 80px;
    top: 0;
    width: 393px;
    text-align: center;
    font-family: "Noto Sans", sans-serif;
    color: var(--ink-white);
  }
  .brand-name--small {
    position: absolute;
    left: 0;
    right: 0;
    top: 70px;
    margin: 0;
    font-size: 17px;
    font-weight: 800;
    line-height: 1;
  }
  .creed-rule {
    position: absolute;
    left: 0;
    top: 89px;
    width: 393px;
    height: 4px;
    background: var(--signal-red);
  }
  .creed-heading {
    position: absolute;
    left: 0;
    top: 96px;
    width: 393px;
    height: 31px;
    margin: 0;
    background: var(--signal-red);
    font-size: 23px;
    font-weight: 700;
    line-height: 31px;
    letter-spacing: 0.3px;
  }
  .creed-list {
    position: absolute;
    left: 0;
    top: 165px;
    width: 393px;
    margin: 0;
    padding: 0;
    list-style: none;
    font-size: 19px;
    font-weight: 700;
    line-height: 24px;
    letter-spacing: 0.4px;
  }
  .creed-list li { margin-bottom: 24px; }
</style>
</head>
<body>
  <main class="cover-spread">
    <svg class="cover-art" viewBox="0 0 1105 775" xmlns="http://www.w3.org/2000/svg">
      <defs>
        <linearGradient id="gold-foil" x1="0" y1="0" x2="0" y2="1">
          <stop offset="0" style="stop-color: var(--gold-light)"/>
          <stop offset="1" style="stop-color: var(--gold-dark)"/>
        </linearGradient>
        <linearGradient id="red-band" x1="0" y1="0" x2="1" y2="1">
          <stop offset="0" style="stop-color: var(--signal-red)"/>
          <stop offset="1" style="stop-color: var(--signal-red-deep)"/>
        </linearGradient>
      </defs>

      <polygon class="red-band" points="0,500 827,602 1105,568 1105,775 0,775" fill="url(#red-band)"/>

      <g class="front-cover">
        <text class="brand-name" x="827" y="66" text-anchor="middle"
              font-family="Noto Sans, sans-serif" font-weight="800" font-size="34" fill="#ffffff">Peak Lantern</text>
        <rect class="brand-rule" x="712" y="74" width="228" height="6" style="fill: var(--signal-red)"/>

        <text class="title-main" x="827" y="224" text-anchor="middle"
              font-family="Oswald, sans-serif" font-weight="500" font-size="150"
              textLength="290" lengthAdjust="spacingAndGlyphs" fill="url(#gold-foil)">PEAK</text>
        <text class="title-main" x="827" y="368" text-anchor="middle"
              font-family="Oswald, sans-serif" font-weight="500" font-size="150"
              textLength="470" lengthAdjust="spacingAndGlyphs" fill="url(#gold-foil)">LANTERN</text>
        <rect class="title-rule" x="712" y="390" width="228" height="6" style="fill: var(--signal-red)"/>

        <text class="title-sub" x="827" y="478" text-anchor="middle"
              font-family="Oswald, sans-serif" font-weight="500" font-size="66"
              letter-spacing="1" style="fill: var(--title-pale)">HORIZON</text>
        <text class="title-sub" x="827" y="548" text-anchor="middle"
              font-family="Oswald, sans-serif" font-weight="500" font-size="66"
              letter-spacing="1" style="fill: var(--title-pale)">LOGBOOK</text>

        <text class="tagline" x="827" y="642" text-anchor="middle"
              font-family="Jost, sans-serif" font-weight="300" font-size="29" fill="#ffffff">A SIMPLE WORKBOOK</text>
        <text class="tagline" x="827" y="671" text-anchor="middle"
              font-family="Jost, sans-serif" font-weight="300" font-size="29" fill="#ffffff">TO TRACK YOUR TRANSFORMATION</text>

        <text class="author-name" x="827" y="734" text-anchor="middle"
              font-family="Oswald, sans-serif" font-weight="500" font-size="50"
              fill="url(#gold-foil)">DALE WRENFOLD</text>
      </g>
    </svg>

    <section class="back-cover">
      <p class="brand-name--small">Peak Lantern</p>
      <div class="creed-rule"></div>
      <h2 class="creed-heading">The Peak Lantern Creed</h2>
      <ul class="creed-list">
        <li>We do things that matter.</li>
        <li>We are skeptical of our limits.</li>
        <li>We don’t fear mistakes,<br>only mediocrity.</li>
        <li>We don’t just think positive<br>thoughts, we act on them</li>
        <li>We know our most important<br>skill is the ability to dream<br>beyond our current abilities.</li>
      </ul>
    </section>
  </main>
</body>
</html>
```